I need professional letterhead for an attorney. I already have my logo (attached). I currently have a project going to get business cards. I would like the letterhead to be classy. It is very important that this letterhead be in a format that I can import it into Microsoft Word 2013. I plan on importing this into Word so I can type my documents directly onto it and electronically send the finished documents to my clients. Thank you very much.

Industry/Entity Type

Attorney

Requirements
Must have
• Here is my info. Please put it all on there:
• Dwight R. Mallory Attorney At Law
• 48613 Brackwell Crescent
• St. Louis, MO 63047
• Telephone: 314-596-2043
• Fax: 800-627-4915
• Email: Dwight@RivermarkWills.com
• Also, I need the ability to import this final design into Microsoft Word 2013 so that I can type directly onto it. I believe I can do that if you hand it over to me as a JPG and a PDF in addition to the other formats. Then I should be able to import it into Word.

```html
<!DOCTYPE html>
<html lang="en">
<head>
<meta charset="utf-8">
<title>Rivermark Wills &amp; Estates LLC – Letterhead</title>
<link href="https://fonts.googleapis.com/css2?family=Carlito:wght@400;700&display=swap" rel="stylesheet">
<style>
  :root {
    --brand-blue: #2a6db5;
    --brand-navy: #1f4f86;
    --band-blue: #cfe0f3;
    --ink: #1c1c1c;
    --paper: #ffffff;
    --mark-faint: #e8f0f9;
  }
  * { box-sizing: border-box; margin: 0; padding: 0; }
  html, body { width: 849px; height: 1200px; overflow: hidden; background: var(--paper); }
  body { font-family: "Carlito", "Calibri", sans-serif; color: var(--ink); }
  .letterhead { position: relative; width: 849px; height: 1200px; }

  .brand { position: absolute; top: 34px; left: 0; width: 100%; display: flex; justify-content: center; align-items: center; gap: 16px; }
  .brand-square { width: 70px; height: 70px; background: var(--brand-blue); }
  .brand-name { color: var(--brand-blue); font-weight: 700; text-transform: uppercase; line-height: 1; }
  .brand-name .line-1 { display: block; font-size: 38px; letter-spacing: 1px; }
  .brand-name .line-2 { display: block; font-size: 26px; letter-spacing: 5px; margin-top: 6px; }

  .faint-mark { position: absolute; left: 274px; top: 380px; width: 300px; height: 300px; border-radius: 50%; background: var(--mark-faint); z-index: 0; }

  .content { position: absolute; top: 160px; left: 62px; width: 725px; font-size: 15px; line-height: 1.47; z-index: 1; }
  .sender { margin-bottom: 36px; }
  .salutation { margin-bottom: 16px; }
  .content p.body { text-align: justify; margin-bottom: 20px; }
  .signature { text-align: right; margin-top: 18px; }

  .footer { position: absolute; left: 0; bottom: 40px; width: 100%; height: 40px; background: var(--band-blue); border-top: 3px solid var(--brand-blue); display: flex; justify-content: space-between; align-items: center; padding: 0 62px; color: var(--brand-navy); font-size: 15px; }
</style>
</head>
<body>
<div class="letterhead">
  <header class="brand">
    <div class="brand-square"></div>
    <div class="brand-name">
      <span class="line-1">Rivermark Wills</span>
      <span class="line-2">&amp; Estates LLC</span>
    </div>
  </header>

  <div class="faint-mark" aria-hidden="true"></div>

  <main class="content">
    <div class="sender">
      Dwight R. Mallory Attorney At Law<br>
      48613 Brackwell Crescent<br>
      St. Louis, MO 63047
    </div>
    <p class="salutation">Dear Jane Doe</p>
    <p class="body">Lorem ipsum dolor sit amet, consectetur adipiscing elit. Nam vestibulum sed libero feugiat interdum. Etiam dapibus molestie lacinia. Donec id commodo erat. Fusce tincidunt tortor in ipsum facilisis, convallis consequat risus viverra. Nam sollicitudin nisi non augue dignissim, molestie dignissim tortor elementum. Mauris urna nisl, sagittis a odio nec, sodales dignissim metus. Nam vestibulum, erat a posuere molestie, nisi tellus accumsan orci, venenatis pellentesque lacus mauris ac turpis. Morbi congue mi sed lacus finibus, ut ultricies risus dapibus. Cras dignissim mauris quis nibh dapibus, quis condimentum odio consequat. Sed pulvinar risus congue tristique dignissim. Maecenas suscipit hendrerit purus, nec porttitor libero commodo eget. Nullam blandit convallis eros, et congue risus vestibulum id. Ut id imperdiet enim.</p>
    <p class="body">Aliquam nec purus neque. Cras efficitur mauris pulvinar posuere dictum. Suspendisse malesuada quam a metus vehicula convallis id vitae tortor. Integer finibus varius erat in auctor. Aliquam erat volutpat. Cras hendrerit ullamcorper est, eget convallis leo finibus vitae. Proin commodo risus urna, at aliquam ante convallis vel. Etiam interdum posuere leo, in volutpat mi sodales et. Suspendisse in lacus justo. Sed porta condimentum ex sit amet tristique.</p>
    <p class="body">Phasellus sed velit lectus. Duis tincidunt id ipsum id ullamcorper. Vivamus porta quam eu metus pharetra convallis. Proin a mauris tortor. Aliquam rhoncus accumsan lectus, bibendum dignissim nisl malesuada in. Phasellus neque lectus, tristique in eleifend ut, rutrum tempor dolor. Aliquam quis lorem non mi sodales dignissim. Fusce accumsan nibh ac sagittis consectetur. Suspendisse lobortis, sapien nec auctor commodo, augue nisl cursus orci, et faucibus ipsum libero ac urna. Aliquam tincidunt venenatis accumsan. Donec condimentum posuere mi, eget cursus nunc malesuada nec. In ut libero scelerisque, posuere eros placerat, hendrerit enim. Cras tempus ante velit, ut dictum tellus euismod facilisis. Maecenas sit amet pellentesque velit.</p>
    <p class="body">Integer sed libero finibus, pharetra dolor vestibulum, auctor metus. Sed nec est sodales, consequat leo ac, malesuada est. Sed pulvinar erat id congue consectetur. Pellentesque habitant morbi tristique senectus et netus et malesuada fames ac turpis egestas. Fusce luctus tellus vel eros viverra volutpat. Aenean id odio in sem congue elementum. Proin quis ipsum augue. Integer egestas justo at magna aliquet faucibus. Nam pellentesque efficitur egestas.</p>
    <div class="signature">
      Dwight R. Mallory<br>
      Attorney At Law
    </div>
  </main>

  <footer class="footer">
    <span>Telephone: 314-596-2043</span>
    <span>Fax: 800-627-4915</span>
    <span>Email: Dwight@RivermarkWills.com</span>
  </footer>
</div>
</body>
</html>
```